Website Design

Hi I would like to invite designers to re design my website .

I would like the below in brief.

On the Welcome Page.

A nice looking technical page distributed into two

SALES on one side and TECHNOLOGY on the other . once the person clicks on either of them they can explore the pages in detail.

I am keen and almost ready with information for the Technology page and would like this to begin kicking ASAP .

my current website is www.brimvoltek.net

Looking forward to seeing your feedback!

Tobiah
Updates

Hi,

 
A little more elaboration on the web front page . I need it to be more techy .

I was looking at a wheel on the Technical side or a spanner and screew driver done on flash .

Just to give you a better idea on what seperated Sales from Technology. 

Computing, Storage , Components , Peripherals , Software , TV & Gaming / Entertainment , Home & Leisure , Software , Gift Vouchers , Phones etc.

Technology .

Solar Power Solutions , Security Systems , Access Control , Automatic Gates & Turnstiles , Home/Office/Hotel Automation, Indoor and Outdoor PABX Telephony, Networking , Electricity Power Meters , IP Based Technology and ETC. 

See attached on the project updates my business card design if it can give you an idea ,also see revised Logo

```html
<!DOCTYPE html>
<html lang="en">
<head>
<meta charset="utf-8">
<title>Brimvoltek – Welcome</title>
<link href="https://fonts.googleapis.com/css2?family=Open+Sans:wght@400;600;700&display=swap" rel="stylesheet">
<style>
:root{
  --red:#d9261c;
  --red-soft:#e04a55;
  --dark:#333333;
  --text:#333;
  --muted:#888;
  --line:#dcdcdc;
  --white:#fff;
  --fb:#3b5998;--tw:#2fa9e0;--gp:#dd4b39;--ig:#8a6a4f;--rss:#f39a1e;--pin:#cb2027;--tb:#35506b;
}
*{box-sizing:border-box;margin:0;padding:0}
html,body{width:837px;height:1200px;overflow:hidden;background:var(--white);font-family:"Open Sans",sans-serif;color:var(--text)}
.page{position:relative;width:837px;height:1200px;border-top:3px solid var(--dark)}
.abs{position:absolute}
.brand{left:87px;top:22px;font-size:36px;font-weight:600;color:var(--red);letter-spacing:.5px}
.social{display:flex;gap:4.5px}
.social span{width:26px;height:26px;border-radius:3px;display:block}
.social.small span{width:23px;height:23px}
.s1{background:var(--fb)}.s2{background:var(--tw)}.s3{background:var(--gp)}.s4{background:var(--ig)}.s5{background:var(--rss)}.s6{background:var(--pin)}.s7{background:var(--tb)}
.nav{left:0;top:83px;width:837px;height:35px;background:var(--dark)}
.nav ul{list-style:none;position:absolute;left:87px;top:0;display:flex;height:35px}
.nav li{color:var(--white);font-size:12px;font-weight:600;line-height:35px;padding:0 12px}
.nav li.active{background:var(--red);padding:0 13px 0 15px}
.search{left:564px;top:7px;width:186px;height:21px;background:#f4f4f4;font-size:9px;color:#555;padding:5px 12px}
.search svg{position:absolute;right:9px;top:5px}
.hero{left:0;top:118px;width:837px;height:278px;background:linear-gradient(90deg,#d7d9dc 0%,#eaebed 50%,#e4e6e8 100%)}
.hero-photo{left:40px;top:0;width:410px;height:278px;background:radial-gradient(ellipse at 55% 55%,#8d8f92 0%,#b8babd 55%,rgba(215,217,220,0) 75%)}
.hero h1{left:467px;top:52px;font-size:23px;font-weight:400;color:var(--red);line-height:27px}
.hero p{left:467px;top:120px;width:256px;font-size:10.5px;line-height:14.5px;color:#222}
.btn{background:var(--red);color:var(--white);font-size:10.5px;font-weight:600;border-radius:3px;text-align:center}
.hero .btn{left:469px;top:197px;width:97px;height:27px;line-height:27px;border:1px solid #b71c13}
.tab{border:1px solid var(--line);border-radius:10px;text-align:center;font-size:19px;color:#777;line-height:49px;height:51px}
.divider{left:359px;top:444px;width:1px;height:506px;background:var(--line)}
.cats{left:87px;top:522px;width:210px}
.cat{border-top:1px solid var(--line);padding:13px 0 0 0}
.cat h3{font-size:13.5px;font-weight:400;color:#444;padding-left:33px;position:relative;height:25px}
.cat h3 svg{position:absolute;left:8px;top:4px}
.cat.closed{height:31.5px;padding-top:7px}
.cat.closed:last-child{border-bottom:1px solid var(--line)}
.cat ul{list-style:none;padding-bottom:7px}
.cat li{font-size:11px;color:#888;line-height:17.2px;padding-left:34px;position:relative;white-space:nowrap}
.cat li::before{content:"";position:absolute;left:10px;top:6px;width:5px;height:5px;border:1px solid #777;border-radius:50%}
.cat li.on{color:var(--red)}
.cat li.on::before{background:var(--red);border-color:var(--red)}
.card{left:424px;top:523px;width:326px;height:427px;border:1px solid var(--line);border-radius:9px}
.card h2{position:absolute;left:0;top:12px;width:100%;text-align:center;font-size:24px;font-weight:400;color:var(--red)}
.rule{position:absolute;left:27px;width:273px;height:1px;background:var(--line)}
.product-img{left:70px;top:66px;width:190px;height:110px;border-radius:6px;background:linear-gradient(180deg,#c9ccd0 0%,#9fb0bd 45%,#42b5dd 70%,#e9506a 80%,#d8d34a 90%,#b9bcbf 100%)}
.card p{position:absolute;left:36px;top:197px;width:262px;font-size:8.9px;line-height:13.2px;color:#444}
.feat{position:absolute;left:36px;top:268px;list-style:none}
.feat li{font-size:10.5px;line-height:14.5px;color:#222;padding-left:13px;position:relative}
.feat li::before{content:"";position:absolute;left:0;top:6px;width:4px;height:4px;border-radius:50%;background:#999}
.card .btn{left:36px;top:379px;width:118px;height:28px;line-height:28px;background:var(--red-soft);border-radius:0;display:flex;align-items:center;justify-content:center;gap:6px}
.info{left:87px;top:982px;width:663px;height:142px;border:1px solid var(--line);border-radius:10px}
.info h4{position:absolute;font-size:19px;font-weight:400;color:var(--red)}
.info .about{position:absolute;left:20px;top:52px;width:370px;font-size:9.3px;line-height:16px;color:#888}
.info .about + .about{top:103px}
.info .vline{position:absolute;left:408px;top:14px;width:1px;height:110px;background:var(--line)}
.contact{position:absolute;left:432px;top:53px;font-size:9.3px;line-height:16px;color:#888}
.contact b{color:#555;font-weight:700}
.footer{left:0;top:1153px;width:837px;height:47px;background:var(--dark);color:var(--white);font-size:9.5px}
.footer .links{position:absolute;left:88px;top:17px}
.footer .copy{position:absolute;right:87px;top:17px}
</style>
</head>
<body>
<div class="page">
  <header>
    <div class="abs brand">Brimvoltek</div>
    <div class="abs social" style="left:542px;top:28px"><span class="s1"></span><span class="s2"></span><span class="s3"></span><span class="s4"></span><span class="s5"></span><span class="s6"></span><span class="s7"></span></div>
  </header>

  <nav class="abs nav">
    <ul><li class="active">DESKTOPS</li><li>LAPTOPS &amp; NOTEBOOKS</li><li>COMPONENTS</li><li>TABLETS</li></ul>
    <div class="abs search">Search.....
      <svg width="11" height="11" viewBox="0 0 11 11"><circle cx="4.5" cy="4.5" r="3.5" fill="none" stroke="#999" stroke-width="1.3"/><line x1="7" y1="7" x2="10" y2="10" stroke="#999" stroke-width="1.5"/></svg>
    </div>
  </nav>

  <section class="abs hero">
    <div class="abs hero-photo" role="img" aria-label="Smiling businessman in a grey suit holding up a smartphone showing the store name, office background"></div>
    <h1 class="abs">Welcome to<br>Brimvoltek</h1>
    <p class="abs">Lorem Ipsum is simply dummy text of the printing and typesetting industry. Lorem Ipsum has been the industry's standard dummy text ever since the 1500s, when an unknown printer took a galley of</p>
    <div class="abs btn">Learn more</div>
  </section>

  <div class="abs tab" style="left:111px;top:444px;width:164px">SALES</div>
  <div class="abs tab" style="left:458px;top:444px;width:242px">TECHNOLOGY</div>
  <div class="abs divider"></div>

  <aside class="abs cats">
    <div class="cat">
      <h3><svg width="11" height="9"><path d="M0 0H11L5.5 8Z" fill="#111"/></svg>Entertainment</h3>
      <ul><li>Novapad Reader</li><li class="on">Tunebox Mini</li><li>Skyline Audio Player</li><li>Quietwave Noise-Canceling Headphones</li><li>Coral Media 300</li></ul>
    </div>
    <div class="cat">
      <h3><svg width="11" height="9"><path d="M0 0H11L5.5 8Z" fill="#111"/></svg>Computing</h3>
      <ul><li>Linkbase Router</li><li>Novapad Tablet</li><li>Ferrow Book 100</li><li>Kestra Mini 700</li><li>Retrobyte 64</li></ul>
    </div>
    <div class="cat closed"><h3><svg width="8" height="11"><path d="M0 0V11L7 5.5Z" fill="#111"/></svg>Communication</h3></div>
    <div class="cat closed"><h3><svg width="8" height="11"><path d="M0 0V11L7 5.5Z" fill="#111"/></svg>Lifestyle</h3></div>
    <div class="cat closed"><h3><svg width="8" height="11"><path d="M0 0V11L7 5.5Z" fill="#111"/></svg>Cameras</h3></div>
    <div class="cat closed"><h3><svg width="8" height="11"><path d="M0 0V11L7 5.5Z" fill="#111"/></svg>Health</h3></div>
  </aside>

  <article class="abs card">
    <h2>Tunebox Touch</h2>
    <div class="rule" style="top:54px"></div>
    <div class="abs product-img" role="img" aria-label="Media player showing a group photo, stacked on colourful players with earbuds"></div>
    <div class="rule" style="top:185px"></div>
    <p>The ClearShot camera lets you take your best shots. Social integration gives you plenty to post about. And, of course, there are endless games to play and endless music to listen to. All on the thinnest, lightest Tunebox Touch ever.</p>
    <div class="rule" style="top:260px"></div>
    <ul class="feat"><li>4-inch HD display</li><li>5-megapixel ClearShot camera</li><li>Music and video</li><li>Dual-core T5 chip</li><li>Tunebox Earbuds</li><li>Game and Apps</li><li>Wireless link</li></ul>
    <div class="abs btn"><svg width="11" height="9" viewBox="0 0 11 9"><path d="M0 3H11L9.5 9H1.5Z M3 3L5.5 0.5L8 3" fill="#fff" stroke="#fff" stroke-width=".8"/></svg>Add to cart</div>
  </article>

  <section class="abs info">
    <h4 style="left:20px;top:16px">About our store</h4>
    <p class="about">Lorem Ipsum is simply dummy text of the printing and typesetting industry. Lorem Ipsum has been the industry's standard dummy text ever since the 1500s, when an unknown printer took a galley of type and scrambled it to make a type specimen</p>
    <p class="about">It has survived not only five centuries, but also the leap into electronic typesetting,</p>
    <div class="vline"></div>
    <h4 style="left:432px;top:16px">Keep in touch</h4>
    <div class="contact"><b>Phone:</b> +12(555)010-2040, +12(555)010-2040<br><b>E-mail:</b> contact@brimvoltek.net</div>
    <div class="abs social small" style="left:432px;top:93px"><span class="s1"></span><span class="s2"></span><span class="s3"></span><span class="s4"></span><span class="s5"></span><span class="s6"></span><span class="s7"></span></div>
  </section>

  <footer class="abs footer">
    <div class="links">Terms of Service &nbsp;|&nbsp; Privacy Policy &nbsp;|&nbsp; Contact us</div>
    <div class="copy">Copyright © 2013 . Brimvoltek. All rights reserved</div>
  </footer>
</div>
</body>
</html>
```